Business Card Design for Concierge business

Hi. I would like to have an elegant, smart business card for my concierge business, called Harbor Concierge. The services I provide are mail management, dog walking, cleaning, car, stylist, personal shopper, running errands, property management, event planning. I was thinking to add my picture but I would like to see options without it as well, if possible.

Thank you.

Business Card Details:
*Designers are to solely use contact information for the business card design. This is not to be used to contact the customer*

Name: Tamsin Heller
mail: quaylineerrands@mailvora.net
Phone: 305-482-9167

Target Market(s)

vacation home owners

Industry/Entity Type

Business

Font styles to use
Serif

Colors

Designer to choose colors to be used in the design.

Requirements
Nice to have
• Could use icons that describe the services I provide for example car, house, key, shopping cart, shopping bags, envelope, champagne glasses, phone, dog etc.

```html
<!DOCTYPE html>
<html lang="en">
<head>
<meta charset="utf-8">
<title>Harbor Concierge – Business Card</title>
<link rel="stylesheet" href="https://fonts.googleapis.com/css2?family=Cinzel:wght@500;600&family=Tinos:wght@400&display=swap">
<style>
  :root {
    --backdrop: #ecebe8;
    --brand-red: #d4202a;
    --brand-red-deep: #9e141c;
    --ink: #1c1c1c;
    --silver: #e4e4e4;
    --paper: #ffffff;
    --paper-shade: #e9e9e9;
    --charcoal: #2b2b2b;
    --photo-top: #8a7a70;
    --photo-bottom: #3c3532;
  }
  * { margin: 0; padding: 0; box-sizing: border-box; }
  html, body { width: 1200px; height: 784px; overflow: hidden; }
  body { background: var(--backdrop); position: relative; font-family: "Tinos", "Times New Roman", serif; }

  .card {
    position: absolute; width: 540px; height: 309px; overflow: hidden;
    box-shadow: 0 10px 26px rgba(0,0,0,.18);
  }
  .card-back { left: 50px; top: 120px; background: linear-gradient(135deg, #e5232d 0%, var(--brand-red) 45%, var(--brand-red-deep) 100%); }
  .card-front { left: 610px; top: 355px; background: linear-gradient(160deg, var(--paper) 0%, var(--paper-shade) 100%); }
  .facets { position: absolute; inset: 0; }

  /* back */
  .back-brand {
    position: absolute; top: 52px; left: 0; right: 0; text-align: center;
    font-family: "Cinzel", "Times New Roman", serif; font-weight: 600;
    font-size: 17px; letter-spacing: 2.5px; color: var(--silver);
  }
  .back-brand .brand-square { display: inline-block; width: 12px; height: 12px; background: var(--silver); margin-right: 10px; vertical-align: 0; }
  .service-list { position: absolute; list-style: none; }
  .service-list.left { left: 30px; top: 100px; }
  .service-list.right { left: 286px; top: 90px; }
  .service {
    display: flex; align-items: center; gap: 12px; height: 32px;
    font-family: "Cinzel", "Times New Roman", serif; font-weight: 500;
    font-size: 11px; letter-spacing: .6px; color: var(--ink);
  }
  .service svg { width: 26px; height: 24px; flex: none; }

  /* front */
  .front-brand {
    position: absolute; left: 40px; top: 112px; white-space: nowrap;
    font-family: "Cinzel", "Times New Roman", serif; font-weight: 600;
    font-size: 19px; letter-spacing: 2px; color: var(--ink);
  }
  .front-brand .brand-square { display: inline-block; width: 13px; height: 13px; background: var(--brand-red); margin-right: 10px; }
  .portrait {
    position: absolute; right: 30px; top: 22px; width: 140px; height: 218px;
    background: linear-gradient(180deg, var(--photo-top), var(--photo-bottom));
  }
  .stripes { position: absolute; inset: 0; }
  .holder-name { position: absolute; left: 40px; top: 180px; font-size: 21px; color: var(--brand-red); }
  .contact { position: absolute; left: 40px; top: 212px; list-style: none; font-size: 16px; color: var(--ink); }
  .contact li { display: flex; align-items: center; gap: 10px; height: 24px; }
  .contact svg { width: 14px; height: 14px; flex: none; }
</style>
</head>
<body>

<section class="card card-back">
  <svg class="facets" viewBox="0 0 540 309" preserveAspectRatio="none" aria-hidden="true">
    <polygon points="0,0 220,0 120,140" fill="#fff" opacity=".06"/>
    <polygon points="300,0 540,0 540,120" fill="#000" opacity=".06"/>
    <polygon points="120,140 330,309 0,309" fill="#000" opacity=".08"/>
    <polygon points="380,130 540,309 300,309" fill="#fff" opacity=".05"/>
  </svg>
  <div class="back-brand"><span class="brand-square"></span>HARBOR CONCIERGE</div>

  <ul class="service-list left">
    <li class="service">
      <svg viewBox="0 0 26 24"><rect x="2" y="5" width="22" height="14" fill="var(--ink)"/><polyline points="2,5 13,13 24,5" fill="none" stroke="#e5232d" stroke-width="1.5"/></svg>
      MAIL MANAGEMENT</li>
    <li class="service">
      <svg viewBox="0 0 26 24"><circle cx="13" cy="12" r="7" fill="var(--ink)"/></svg>
      DOG WALKING</li>
    <li class="service">
      <svg viewBox="0 0 26 24"><rect x="4" y="9" width="18" height="12" fill="var(--ink)"/><rect x="9" y="3" width="8" height="6" fill="var(--ink)"/></svg>
      CLEANING</li>
    <li class="service">
      <svg viewBox="0 0 26 24"><path d="M1 16 L4 10 L9 9 L13 6 L20 6 L24 11 L25 16 Z" fill="var(--ink)"/><circle cx="7" cy="17" r="2.5" fill="var(--ink)"/><circle cx="19" cy="17" r="2.5" fill="var(--ink)"/></svg>
      CAR</li>
    <li class="service">
      <svg viewBox="0 0 26 24"><line x1="4" y1="4" x2="20" y2="20" stroke="var(--ink)" stroke-width="2"/><line x1="20" y1="4" x2="4" y2="20" stroke="var(--ink)" stroke-width="2"/><circle cx="4" cy="20" r="3" fill="none" stroke="var(--ink)" stroke-width="2"/><circle cx="20" cy="20" r="3" fill="none" stroke="var(--ink)" stroke-width="2"/></svg>
      STYLIST</li>
  </ul>

  <ul class="service-list right">
    <li class="service">
      <svg viewBox="0 0 26 24"><polyline points="1,3 5,3 8,15 21,15 24,7 6,7" fill="none" stroke="var(--ink)" stroke-width="2"/><circle cx="9" cy="20" r="2" fill="var(--ink)"/><circle cx="20" cy="20" r="2" fill="var(--ink)"/></svg>
      PERSONAL SHOPPER</li>
    <li class="service">
      <svg viewBox="0 0 26 24"><rect x="5" y="8" width="16" height="14" fill="var(--ink)"/><path d="M9 8 V5 a4 4 0 0 1 8 0 V8" fill="none" stroke="var(--ink)" stroke-width="2"/></svg>
      RUNNING ERRANDS</li>
    <li class="service">
      <svg viewBox="0 0 26 24"><polygon points="13,2 24,11 2,11" fill="var(--ink)"/><rect x="5" y="11" width="16" height="11" fill="var(--ink)"/><rect x="11" y="15" width="4" height="7" fill="#e5232d"/></svg>
      PROPERTY MANAGEMENT</li>
    <li class="service">
      <svg viewBox="0 0 26 24"><path d="M4 3 H11 L10 10 a3 3 0 0 1 -5 0 Z" fill="var(--ink)"/><line x1="7.5" y1="12" x2="7.5" y2="20" stroke="var(--ink)" stroke-width="1.5"/><path d="M15 3 H22 L21 10 a3 3 0 0 1 -5 0 Z" fill="var(--ink)"/><line x1="18.5" y1="12" x2="18.5" y2="20" stroke="var(--ink)" stroke-width="1.5"/></svg>
      EVENT PLANNING</li>
  </ul>
</section>

<section class="card card-front">
  <svg class="facets" viewBox="0 0 540 309" preserveAspectRatio="none" aria-hidden="true">
    <polygon points="0,0 200,0 90,120" fill="#000" opacity=".03"/>
    <polygon points="200,0 380,0 300,150" fill="#000" opacity=".025"/>
    <polygon points="0,180 160,309 0,309" fill="#000" opacity=".04"/>
    <polygon points="160,140 330,309 120,309" fill="#fff" opacity=".5"/>
  </svg>

  <div class="front-brand"><span class="brand-square"></span>HARBOR CONCIERGE</div>

  <div class="portrait" role="img" aria-label="Portrait photograph of Tamsin Heller"></div>

  <svg class="stripes" viewBox="0 0 540 309" preserveAspectRatio="none" aria-hidden="true">
    <polygon points="300,248 540,232 540,240 300,256" fill="var(--brand-red)"/>
    <polygon points="240,274 540,254 540,258 240,278" fill="var(--brand-red)"/>
    <polygon points="0,290 70,290 62,300 0,300" fill="var(--charcoal)"/>
    <polygon points="74,290 540,276 540,280 74,294" fill="var(--brand-red)"/>
  </svg>

  <div class="holder-name">Tamsin Heller</div>
  <ul class="contact">
    <li>
      <svg viewBox="0 0 14 14"><path d="M2 1 L5 1 L6 4 L4 5.5 Q5.5 8.5 8.5 10 L10 8 L13 9 L13 12 Q13 13 12 13 Q1 12 1 2 Q1 1 2 1 Z" fill="var(--brand-red)"/></svg>
      305-482-9167</li>
    <li>
      <svg viewBox="0 0 14 14"><rect x="1" y="3" width="12" height="9" fill="var(--brand-red)"/><polyline points="1,3 7,8 13,3" fill="none" stroke="#fff" stroke-width="1.2"/></svg>
      quaylineerrands@mailvora.net</li>
  </ul>
</section>

</body>
</html>
```